Simple but elegant business card/logo design for exclusive beauty business

We need a logo designed for a new elegant and exclusive beauty business called "R". The logo itself should be a stylistic and custom design for the letter "R". We would like the business card to have the logo as the centrepiece on a clean background. Gold Logo on black background or silver on white background.

The business card details should be displayed centre of the card. Details are as follows:

Tamsin Earle
Facebook: /shinesoftlyr
Instagram: /shinesoftlyr

The words "Shine Softly" should also appear somewhere on the card.

Industry/Entity Type

Business

Logo Text

G

Requirements
Must have
• Design must be simple, clean and elegant
Should not have
• The design should not be cluttered

```html
<!DOCTYPE html>
<html lang="en">
<head>
<meta charset="utf-8">
<title>Shine Softly – Business Card</title>
<link rel="stylesheet" href="https://fonts.googleapis.com/css2?family=Mulish:wght@400;600;700&display=swap">
<style>
  :root {
    --backdrop: #2a2a2a;
    --card: #e9e9e9;
    --card-edge: #dcdcdc;
    --ink: #555555;
    --ink-soft: #6a6a6a;
    --rule: #5a5a5a;
    --mark: #bdbdbd;
  }
  html, body {
    margin: 0;
    padding: 0;
    width: 1200px;
    height: 600px;
    overflow: hidden;
    background: var(--backdrop);
    font-family: "Mulish", Arial, sans-serif;
  }
  .canvas {
    position: relative;
    width: 1200px;
    height: 600px;
    background: var(--backdrop);
  }
  .card {
    position: absolute;
    top: 164px;
    width: 466px;
    height: 272px;
    border-radius: 14px;
    background: var(--card);
    box-shadow: inset 0 0 0 1px var(--card-edge);
    overflow: hidden;
  }
  .card--front { left: 123px; }
  .card--back { left: 613px; width: 464px; }

  .tagline {
    position: absolute;
    left: 38px;
    top: 20px;
    margin: 0;
    font-size: 20px;
    font-weight: 400;
    color: var(--ink);
    letter-spacing: 0.2px;
  }
  .tagline strong { font-weight: 700; }

  .monogram {
    position: absolute;
    font-family: "Mulish", Arial, sans-serif;
    font-weight: 400;
    color: var(--ink-soft);
    line-height: 1;
  }
  .monogram--corner {
    right: 44px;
    top: 22px;
    font-size: 64px;
  }
  .monogram--centre {
    left: 0;
    right: 0;
    top: 50%;
    transform: translateY(-50%);
    text-align: center;
    font-size: 130px;
    color: var(--mark);
  }

  .holder {
    position: absolute;
    left: 39px;
    top: 156px;
    margin: 0;
    font-size: 20px;
    font-weight: 400;
    color: var(--ink);
  }
  .divider {
    position: absolute;
    left: 40px;
    top: 188px;
    width: 388px;
    height: 2px;
    background: var(--rule);
  }
  .contact {
    position: absolute;
    display: flex;
    align-items: center;
    gap: 6px;
    font-size: 13px;
    line-height: 16px;
    color: var(--ink);
  }
  .contact--phone { left: 40px; top: 195px; }
  .contact--email { right: 38px; top: 195px; }
  .contact--social-left { left: 40px; top: 227px; }
  .contact--social-right { right: 38px; top: 227px; }
  .contact svg { display: block; color: var(--ink-soft); }
  .social-square {
    width: 10px;
    height: 10px;
    background: var(--ink-soft);
    border-radius: 1px;
  }
</style>
</head>
<body>
<main class="canvas">
  <section class="card card--front" aria-label="Card front">
    <h2 class="tagline">Shine <strong>Softly</strong></h2>
    <span class="monogram monogram--corner">R</span>
    <h1 class="holder">Tamsin Earle</h1>
    <div class="divider"></div>

    <div class="contact contact--phone">
      <svg width="12" height="10" viewBox="0 0 12 10" aria-hidden="true">
        <path d="M1 3 Q6 0 11 3 L10 5 L8 4 L8 3 Q6 2.5 4 3 L4 4 L2 5 Z" fill="currentColor"/>
        <rect x="2.5" y="5" width="7" height="4.5" rx="0.8" fill="currentColor"/>
      </svg>
      <span>000 000 0000</span>
    </div>
    <div class="contact contact--email">
      <span>youremail@xyz.com</span>
      <svg width="13" height="9" viewBox="0 0 13 9" aria-hidden="true">
        <rect x="0.5" y="0.5" width="12" height="8" fill="currentColor"/>
        <path d="M0.5 0.5 L6.5 5 L12.5 0.5" fill="none" stroke="#e9e9e9" stroke-width="1"/>
      </svg>
    </div>
    <div class="contact contact--social-left">
      <span class="social-square"></span>
      <span>/shinesoftlyr</span>
    </div>
    <div class="contact contact--social-right">
      <span>/shinesoftlyr</span>
      <span class="social-square"></span>
    </div>
  </section>

  <section class="card card--back" aria-label="Card back">
    <span class="monogram monogram--centre">R</span>
  </section>
</main>
</body>
</html>
```